Business Card Design

Electronic Security Installation Specialists

Check out our website at www.brightpulsellc.com to see what we do.

Industry/Entity Type

Business

Contact Information for Business Card

Bright Pulse
Marianne Tolbert
218 Orchard Bend
Cedar Hollow, WV 26918

Colors
3176b5
0455a3
ffffff

```html
<!DOCTYPE html>
<html lang="en">
<head>
<meta charset="utf-8">
<title>Bright Pulse — Business Card</title>
<link href="https://fonts.googleapis.com/css2?family=Open+Sans:wght@400;600&display=swap" rel="stylesheet">
<style>
  :root {
    --brand-blue: #3176b5;
    --brand-deep: #0455a3;
    --brand-navy: #033f7c;
    --paper: #ffffff;
    --ink: #4a4a4a;
    --ink-soft: #6b6b6b;
    --stage: #ecedef;
  }
  * { box-sizing: border-box; margin: 0; padding: 0; }
  html, body {
    width: 1200px; height: 913px; overflow: hidden;
    background: var(--stage);
    font-family: "Open Sans", Arial, sans-serif;
  }
  .stage {
    position: relative; width: 1200px; height: 913px;
    display: flex; align-items: center; justify-content: center; gap: 60px;
  }
  .card {
    width: 520px; height: 297px; position: relative;
    box-shadow: 0 6px 18px rgba(0,0,0,.18);
  }
  .card--front {
    background: linear-gradient(160deg, var(--brand-blue) 0%, var(--brand-deep) 55%, var(--brand-navy) 100%);
    display: flex; align-items: center; justify-content: center; gap: 14px;
  }
  .brand-dot {
    width: 22px; height: 22px; border-radius: 50%;
    background: var(--paper);
  }
  .brand-name {
    font-weight: 600; font-size: 40px; color: var(--paper); letter-spacing: .5px;
  }
  .card--back { background: var(--paper); }
  .back-brand {
    position: absolute; left: 40px; top: 128px;
    display: flex; align-items: center; gap: 10px;
  }
  .back-brand .brand-dot { width: 16px; height: 16px; background: var(--brand-deep); }
  .back-brand .brand-name { font-size: 26px; color: var(--brand-deep); }
  .contact {
    position: absolute; left: 300px; top: 40px;
    font-size: 12.5px; color: var(--ink); line-height: 1.5;
  }
  .contact__name { font-weight: 600; font-size: 17px; color: var(--brand-blue); }
  .contact__title { color: var(--ink-soft); margin-bottom: 40px; }
  .contact__address { margin-bottom: 8px; }
  .contact__row { display: flex; align-items: center; gap: 8px; }
  .contact__row svg { width: 11px; height: 11px; fill: var(--brand-deep); flex: none; }
  .contact__web { color: var(--brand-blue); }
</style>
</head>
<body>
<main class="stage">
  <section class="card card--front" aria-label="Card front">
    <span class="brand-dot"></span>
    <span class="brand-name">Bright Pulse</span>
  </section>

  <section class="card card--back" aria-label="Card back">
    <div class="back-brand">
      <span class="brand-dot"></span>
      <span class="brand-name">Bright Pulse</span>
    </div>
    <div class="contact">
      <p class="contact__name">Marianne Tolbert</p>
      <p class="contact__title">Managing Director</p>
      <p class="contact__address">218 Orchard Bend<br>Cedar Hollow, WV 26918</p>
      <p class="contact__row">
        <svg viewBox="0 0 12 12" aria-hidden="true"><path d="M2.5 1h2l1 2.5-1.3 1a6 6 0 0 0 3.3 3.3l1-1.3L11 7.5v2A1.5 1.5 0 0 1 9.5 11 8.5 8.5 0 0 1 1 2.5 1.5 1.5 0 0 1 2.5 1z"/></svg>
        304-555-0182
      </p>
      <p class="contact__row">
        <svg viewBox="0 0 12 12" aria-hidden="true"><path d="M1 2.5h10v7H1z M1 2.5l5 4 5-4" fill="none" style="stroke:var(--brand-deep)" stroke-width="1.2"/></svg>
        m.tolbert@brightpulsellc.com
      </p>
      <p class="contact__row contact__web">
        <svg viewBox="0 0 12 12" aria-hidden="true"><circle cx="6" cy="6" r="4.8" fill="none" style="stroke:var(--brand-deep)" stroke-width="1.1"/><path d="M1.2 6h9.6M6 1.2c-2.4 2.8-2.4 6.8 0 9.6M6 1.2c2.4 2.8 2.4 6.8 0 9.6" fill="none" style="stroke:var(--brand-deep)" stroke-width="1"/></svg>
        www.brightpulsellc.com
      </p>
    </div>
  </section>
</main>
</body>
</html>
```